TRI FOLD BROCHURE

I need a trifold brochure designed for my carpet cleaning company. It will be specifically for realtors and real estate attorneys. I have the text content I need in the brochure available as well as the company logo and a spotted dog picture we use in most of our marketing.

Industry/Entity Type

Real Estate

```html
<!DOCTYPE html>
<html lang="en">
<head>
<meta charset="utf-8">
<title>Gleamline Floor Care – Tri-Fold Brochure</title>
<link href="https://fonts.googleapis.com/css2?family=Bebas+Neue&family=Lato:wght@400;700&display=swap" rel="stylesheet">
<style>
  :root {
    --bg: #e4e4e4;
    --blue-top: #185a9c;
    --blue-mid: #1a4f8c;
    --blue-bottom: #1c3a6e;
    --white: #ffffff;
    --room-light: #e9e6e1;
    --room-dark: #b9b4ac;
    --family-light: #d8d6d2;
    --family-dark: #5c5a58;
  }
  * { box-sizing: border-box; margin: 0; padding: 0; }
  html, body { width: 1200px; height: 982px; overflow: hidden; }
  body {
    background: var(--bg);
    font-family: 'Lato', sans-serif;
    color: var(--white);
    display: flex;
    align-items: center;
    justify-content: center;
  }
  .brochure {
    display: flex;
    width: 1020px;
    height: 788px;
    box-shadow: 0 6px 24px rgba(0,0,0,0.18);
  }
  .panel {
    width: 340px;
    height: 100%;
    display: flex;
    flex-direction: column;
    background: linear-gradient(180deg, var(--blue-top) 0%, var(--blue-mid) 55%, var(--blue-bottom) 100%);
    position: relative;
  }
  .panel + .panel { border-left: 1px solid rgba(0,0,0,0.12); }
  .photo { width: 100%; flex-shrink: 0; }
  .photo--room {
    height: 300px;
    background: linear-gradient(160deg, var(--white) 0%, var(--room-light) 45%, var(--room-dark) 100%);
  }
  .photo--family {
    height: 360px;
    background: linear-gradient(180deg, var(--family-light) 0%, #a9a7a3 50%, var(--family-dark) 100%);
  }
  .photo-rule { height: 8px; background: var(--white); flex-shrink: 0; }
  .headline {
    font-family: 'Bebas Neue', sans-serif;
    font-weight: 400;
    text-align: center;
    line-height: 1.02;
    letter-spacing: 0.5px;
  }
  .panel--intro .headline { font-size: 34px; margin: 34px 30px 18px; }
  .body-copy {
    font-size: 12.5px;
    line-height: 1.5;
    text-align: center;
    margin: 0 28px;
  }
  .body-copy p + p { margin-top: 2px; }
  .panel--contact { justify-content: center; align-items: center; }
  .brand {
    display: flex;
    align-items: center;
    gap: 10px;
    font-family: 'Bebas Neue', sans-serif;
    font-size: 36px;
    letter-spacing: 1.5px;
    color: var(--white);
    line-height: 1;
  }
  .brand-dot { width: 14px; height: 14px; border-radius: 50%; background: var(--white); }
  .contact {
    margin-top: 40px;
    font-family: 'Bebas Neue', sans-serif;
    font-size: 26px;
    line-height: 1.08;
    text-align: center;
    letter-spacing: 0.5px;
  }
  .contact .web { margin-top: 14px; font-size: 25px; }
  .panel--cover { align-items: center; }
  .panel--cover .headline { font-size: 32px; margin: 30px 28px 0; }
  .panel--cover .brand { margin-top: 48px; }
</style>
</head>
<body>
  <main class="brochure">
    <section class="panel panel--intro">
      <div class="photo photo--room" role="img" aria-label="Bright living room with light carpet, sofa and tall windows"></div>
      <div class="photo-rule"></div>
      <h2 class="headline">Reasons Homeowners<br>Love Gleamline<br>Floor Care</h2>
      <div class="body-copy">
        <p>No cleaning method can promise 100% removal of contaminants in your carpet.</p>
        <p>However, our proprietary cleaning system has been repeatedly tested and proven to produce results that are at least 25% cleaner than even the most powerful steam cleaning systems available!</p>
      </div>
    </section>

    <section class="panel panel--contact">
      <div class="brand"><span class="brand-dot"></span>Gleamline Floor Care</div>
      <div class="contact">
        <p>Call Today</p>
        <p>877-555-0142</p>
        <p>877-NO-STAIN</p>
        <p class="web">www.gleamlinefloorcare.com</p>
      </div>
    </section>

    <section class="panel panel--cover">
      <div class="photo photo--family" role="img" aria-label="Smiling family lying together on a soft grey carpet"></div>
      <div class="photo-rule" style="width:100%"></div>
      <h1 class="headline">Your customers want the best,<br>therefore seek carpet<br>in top condition</h1>
      <div class="brand"><span class="brand-dot"></span>Gleamline Floor Care</div>
    </section>
  </main>
</body>
</html>
```